Creative Business Card for my Sail Boat.. Tide & Time

Going to order PLASTIC business cards for my boat.. she is a sailing vessel catamaran named Tide & Time..

Target Market(s)

to impress other boaters with a unique designed plastic card

Contact Information for Business Card

S/V Tide & Time
Captain Owen Marsh
marsh@owen.example
Mobile/WhatsApp 1-555-318-7062
www.sailtideandtime.example

Requirements
Must have
• Cool colors. logo.. and info in Business Card Details.. Thanks! Utilize clear or cloudy plastic in design. Thanks

```html
<!DOCTYPE html>
<html lang="en">
<head>
<meta charset="utf-8">
<title>Tide &amp; Time — Business Card</title>
<link rel="stylesheet" href="https://fonts.googleapis.com/css2?family=Arimo:wght@400;700&family=Montserrat:wght@400&display=swap">
<style>
  :root {
    --page-bg: #e7e3e1;
    --frost: #f2eaea;
    --frost-edge: #e4d9d8;
    --divider: #b9aca7;
    --brown: #52280f;
    --logo-ink: #4a2812;
    --logo-dot: #3a9a45;
    --text-light: #ffffff;
  }
  * { box-sizing: border-box; margin: 0; padding: 0; }
  html, body {
    width: 1200px;
    height: 900px;
    overflow: hidden;
    background: var(--page-bg);
  }
  .card {
    position: absolute;
    left: 150px;
    top: 172px;
    width: 900px;
    height: 556px;
    display: flex;
    box-shadow: 0 12px 30px rgba(60, 30, 20, 0.18);
  }
  .card-front {
    width: 442px;
    height: 100%;
    background: linear-gradient(160deg, #f6f0f0 0%, var(--frost) 55%, var(--frost-edge) 100%);
    display: flex;
    align-items: center;
    justify-content: center;
  }
  .card-divider {
    width: 8px;
    height: 100%;
    background: var(--divider);
  }
  .card-back {
    flex: 1;
    height: 100%;
    background: var(--brown);
    color: var(--text-light);
    position: relative;
  }
  .brand {
    display: flex;
    align-items: center;
    gap: 14px;
  }
  .brand-name {
    font-family: "Arimo", Arial, sans-serif;
    font-weight: 700;
    font-size: 50px;
    color: var(--logo-ink);
    letter-spacing: -0.5px;
  }
  .brand-dot {
    width: 40px;
    height: 40px;
    border-radius: 50%;
    background: var(--logo-dot);
  }
  .captain {
    position: absolute;
    left: 32px;
    top: 96px;
    font-family: "Arimo", Arial, sans-serif;
  }
  .captain-name {
    font-weight: 700;
    font-size: 37px;
    line-height: 1;
    letter-spacing: 0.3px;
  }
  .captain-title {
    font-weight: 400;
    font-size: 24px;
    margin-top: 3px;
  }
  .contact-list {
    position: absolute;
    left: 30px;
    top: 320px;
    list-style: none;
    font-family: "Montserrat", Arial, sans-serif;
    font-size: 20px;
  }
  .contact-item {
    display: flex;
    align-items: center;
    gap: 12px;
    height: 34px;
    letter-spacing: 0.4px;
    white-space: nowrap;
  }
  .contact-icon {
    width: 28px;
    height: 26px;
    flex: none;
  }
</style>
</head>
<body>
  <div class="card">
    <section class="card-front">
      <div class="brand">
        <span class="brand-name">Tide &amp; Time</span>
        <span class="brand-dot"></span>
      </div>
    </section>
    <div class="card-divider"></div>
    <section class="card-back">
      <div class="captain">
        <p class="captain-name">OWEN MARSH</p>
        <p class="captain-title">Captain</p>
      </div>
      <ul class="contact-list">
        <li class="contact-item">
          <svg class="contact-icon" viewBox="0 0 28 26" aria-hidden="true">
            <rect x="1" y="5" width="26" height="17" fill="#fff"/>
            <path d="M1 5 L14 15 L27 5 M1 22 L11 13 M27 22 L17 13" stroke="#52280f" stroke-width="2" fill="none"/>
          </svg>
          <span>marsh@owen.example</span>
        </li>
        <li class="contact-item">
          <svg class="contact-icon" viewBox="0 0 28 26" aria-hidden="true">
            <rect x="8" y="1" width="13" height="24" rx="2" fill="none" stroke="#fff" stroke-width="2.2"/>
            <rect x="10" y="4" width="9" height="15" fill="#fff"/>
            <circle cx="14.5" cy="22" r="1.3" fill="#fff"/>
          </svg>
          <span>1-555-318-7062</span>
        </li>
        <li class="contact-item">
          <svg class="contact-icon" viewBox="0 0 28 26" aria-hidden="true">
            <circle cx="14" cy="13" r="11" fill="none" stroke="#fff" stroke-width="2.4"/>
          </svg>
          <span>1-555-318-7062</span>
        </li>
        <li class="contact-item">
          <svg class="contact-icon" viewBox="0 0 28 26" aria-hidden="true">
            <g fill="none" stroke="#fff" stroke-width="1.8">
              <circle cx="14" cy="13" r="11"/>
              <ellipse cx="14" cy="13" rx="5" ry="11"/>
              <path d="M3 13 H25 M5 7 H23 M5 19 H23 M14 2 V24"/>
            </g>
          </svg>
          <span>www.sailtideandtime.example</span>
        </li>
      </ul>
    </section>
  </div>
</body>
</html>
```